wedding photography website for top wedding photographer

I have a website right now that is barely working. I want the photos to maybe all the photos lined up horizontally and you scroll to see the images. I have an orange logo and want it to be dark grey. I also need a page for publications (I have those as scans) and a link to an About page.

Target Market(s)

wedding planners and bride

Industry/Entity Type

Wedding Photography

Coding

Coded - Design and coding required

Number of Pages Required

5+ page

Font styles to use
Serif
Sans Serif

Colors
ffffff
474747

Requirements
Must have
• easy to navigate, always want the instagram and contact info readily available, should be clean and modern and let the photos stand out. it's wedding photos but i don't want it to feel girly or prissy.
Nice to have
• possibly could be one big photo on the home page, then click it to go into all the other photos. want page options on the home page and every page
Should not have
• nothing fussy or quaint, want this to be the "Copper Ladle" restaurant of wedding photography

```html
<!DOCTYPE html>
<html lang="en">
<head>
<meta charset="utf-8">
<title>About Me</title>
<link rel="stylesheet" href="https://fonts.googleapis.com/css2?family=Dosis:wght@300;400;500;600&display=swap">
<style>
  :root {
    --bg: #ffffff;
    --ink: #1c1c1c;
    --body: #5a5a5a;
    --accent: #e8601f;
    --ghost: #e6e6e6;
    --photo-warm: #b9a48a;
    --photo-mono: #4a4a4a;
  }
  * { box-sizing: border-box; margin: 0; padding: 0; }
  html, body { width: 1200px; height: 492px; overflow: hidden; background: var(--bg); }
  body { position: relative; font-family: "Dosis", sans-serif; color: var(--body); }

  .photo { position: absolute; display: block; }
  .photo--hero-tail { left: 794px; top: 0; width: 327px; height: 50px;
    background: linear-gradient(90deg, #1e1e1e 0%, #6d6d6d 55%, #2a2a2a 100%); }
  .photo--couple-kiss { left: 85px; top: 141px; width: 201px; height: 157px; z-index: 1;
    background: linear-gradient(135deg, #3c3a35 0%, #c9b9a2 45%, #e9e1d6 70%, #8a7a66 100%); }
  .photo--couple-toast { left: 236px; top: 232px; width: 201px; height: 157px; z-index: 2;
    background: linear-gradient(120deg, #1a1a1a 0%, #3d3d3d 45%, #9c9c9c 75%, #e0e0e0 100%); }
  .photo--ring-bearers { left: 368px; top: 125px; width: 240px; height: 189px; z-index: 3;
    background: linear-gradient(140deg, #d9cdb8 0%, #f1ece4 40%, #b89c72 75%, #8d7556 100%); }

  .about { position: absolute; left: 616px; top: 0; width: 505px; }

  .about__heading { position: absolute; left: 0; top: 135px; width: 505px; height: 56px; text-align: center; }
  .about__ghost { position: absolute; left: 0; right: 0; top: 0; font-size: 58px; font-weight: 500;
    letter-spacing: 4px; color: var(--ghost); line-height: 56px; }
  .about__title { position: absolute; left: 181px; top: 6px; width: 142px; height: 40px;
    font-size: 20px; font-weight: 600; letter-spacing: 2px; color: var(--ink);
    line-height: 40px; text-align: center; }
  .about__title em { font-style: normal; color: var(--accent); }
  .about__brackets { position: absolute; left: 181px; top: 6px; }

  .about__text { position: absolute; left: 0; width: 505px; font-size: 14.5px; font-weight: 400;
    letter-spacing: 1px; line-height: 22px; }
  .about__text--first { top: 209px; }
  .about__text--second { top: 305px; }

  .clients__label { position: absolute; left: 0; top: 359px; font-size: 16px; font-weight: 600;
    letter-spacing: 2px; color: var(--ink); }
  .clients__list { position: absolute; top: 392px; list-style: none; font-size: 15px;
    letter-spacing: 1.2px; line-height: 22px; }
  .clients__list--left { left: 0; }
  .clients__list--right { left: 252px; }

  .back-to-top { position: absolute; left: 1124px; top: 432px; width: 45px; height: 45px;
    background: var(--accent); display: flex; align-items: center; justify-content: center; }
</style>
</head>
<body>
  <div class="photo photo--hero-tail" role="img" aria-label="Black and white wedding photograph of clasped hands"></div>

  <div class="photo photo--couple-kiss" role="img" aria-label="Bride and groom in a cowboy hat sharing a kiss"></div>
  <div class="photo photo--couple-toast" role="img" aria-label="Black and white photo of a couple toasting beside the wedding cake"></div>
  <div class="photo photo--ring-bearers" role="img" aria-label="Young ring bearers in white suits holding a dried bouquet"></div>

  <section class="about">
    <div class="about__heading">
      <span class="about__ghost" aria-hidden="true">ABOUT ME</span>
      <svg class="about__brackets" width="142" height="40" viewBox="0 0 142 40" aria-hidden="true">
        <g fill="none" stroke="#e8601f" stroke-width="1.3">
          <path d="M8 0.7 H0.7 V39.3 H8"/>
          <path d="M134 0.7 H141.3 V39.3 H134"/>
        </g>
      </svg>
      <h2 class="about__title">ABOUT <em>ME</em></h2>
    </div>

    <p class="about__text about__text--first">My mother had a natural talent for portraiture and I was her first model, donning Swedish outfits (complete with caps and aprons!) and posing in our 200-acre woods. She had a make-shift darkroom where she processed the film and printed photographs.</p>
    <p class="about__text about__text--second">The magic of the darkroom and the beauty of the still image are what inspired me to become a photographer.</p>

    <h3 class="clients__label">PARTIAL CLIENT LIST:-</h3>
    <ul class="clients__list clients__list--left">
      <li>Clara Whitfield</li>
      <li>Martin Delacroix</li>
      <li>Owen Marchetti</li>
      <li>Sofia Valdemar</li>
      <li>Jolene Harper</li>
    </ul>
    <ul class="clients__list clients__list--right">
      <li>Danny Korbel</li>
      <li>Harold Brenner</li>
      <li>Lt. Gov. Calvin Moreau</li>
      <li>Natalie Rowan</li>
    </ul>
  </section>

  <a class="back-to-top" href="#" aria-label="Back to top">
    <svg width="16" height="16" viewBox="0 0 16 16" aria-hidden="true">
      <g fill="none" stroke="#ffffff" stroke-width="2.2" stroke-linecap="square">
        <path d="M3 8 L8 3 L13 8"/>
        <path d="M3 14 L8 9 L13 14"/>
      </g>
    </svg>
  </a>
</body>
</html>
```